Business Card Design

I need a business card for my resume writing business. I have a logo that Im not keen on anymore so I would like the business card to use my photo instead of a logo. I am for mid career and trades resumes and prefer not to do executive resumes so don't need to aim for exectives. I would like it to be colourful. I like bright sky blue and maybe some pink or purple but primarily bright sky blue. I don't like green and Im keen see a fair bit of white on the card. As I have a photo to go it, it will need to go on a white background.

Target Market(s)

mid range careers. Not executives

Industry/Entity Type

Business

Contact Information for Business Card

Wyn Marchetti
Resume Writer
Clear Path CVs
27 The Lanyard
HARWOOD NSW 2465
wyn@clearpathcvs.com.au
0417362958
www.clearpathcvs.com.au

Requirements
Nice to have
• Maybe colours similar to my website - www.clearpathcvs.com.au but not with any black on it.
Should not have
• No green or dark colours

```html
<!DOCTYPE html>
<html lang="en">
<head>
<meta charset="utf-8">
<title>Clear Path CVs – Business Card</title>
<link href="https://fonts.googleapis.com/css2?family=Noto+Sans:wght@400&display=swap" rel="stylesheet">
<style>
  :root {
    --card-bg: #ffffff;
    --sky: #16a2ea;
    --sky-deep: #0b86cc;
    --accent-pink: #d9539a;
    --accent-purple: #8a4fbf;
    --portrait-pink: #e46aa8;
    --portrait-rose: #f3b6d4;
    --portrait-skin: #c98a5c;
    --portrait-hair: #8a5534;
  }
  html, body {
    margin: 0;
    padding: 0;
    overflow: hidden;
    background: var(--card-bg);
  }
  .card {
    position: relative;
    width: 1200px;
    height: 725px;
    background: var(--card-bg);
    font-family: "Noto Sans", Verdana, sans-serif;
    overflow: hidden;
  }
  .portrait {
    position: absolute;
    left: 127px;
    top: 61px;
    width: 192px;
    height: 255px;
    border-radius: 80px 80px 0 0;
    background: linear-gradient(180deg,
      var(--portrait-hair) 0%,
      var(--portrait-skin) 22%,
      var(--portrait-skin) 45%,
      var(--portrait-pink) 62%,
      var(--portrait-rose) 100%);
  }
  .writer-name {
    position: absolute;
    left: 91px;
    top: 320px;
    margin: 0;
    font-size: 37px;
    font-weight: 400;
    line-height: 1;
    letter-spacing: 0.5px;
    color: var(--accent-purple);
  }
  .writer-role {
    position: absolute;
    left: 93px;
    top: 368px;
    margin: 0;
    font-size: 27px;
    line-height: 1;
    letter-spacing: 0.4px;
    color: var(--accent-pink);
  }
  .business-name {
    position: absolute;
    left: 478px;
    top: 282px;
    margin: 0;
    font-size: 62px;
    font-weight: 400;
    line-height: 1;
    letter-spacing: 1px;
    white-space: nowrap;
    color: var(--sky);
  }
  .contact {
    position: absolute;
    left: 91px;
    top: 480px;
    margin: 0;
    font-style: normal;
    font-size: 27px;
    line-height: 35.5px;
    letter-spacing: 0.4px;
    color: var(--sky-deep);
  }
  .contact span { display: block; }
</style>
</head>
<body>
  <div class="card">
    <div class="portrait" role="img" aria-label="Portrait photo of Wyn Marchetti in a pink top"></div>
    <h1 class="writer-name">Wyn Marchetti</h1>
    <p class="writer-role">Resumes Writer</p>
    <h2 class="business-name">Clear Path CVs</h2>
    <address class="contact">
      <span>27 The Lanyard</span>
      <span>HARWOOD NSW 2465</span>
      <span>Phone: 0417362958</span>
      <span>Email: wyn@clearpathcvs.com.au</span>
      <span>Web: www.clearpathcvs.com.au</span>
    </address>
  </div>
</body>
</html>
```